Professional and creative business card design for recruiting service providers

Our company supports German medium-sized companies in filling vacancies promptly. For this we use social media marketing and bring our customers into the visibility.

We want a professional but also creative design for our business cards.

Please look at valdringer-kollegen.de to get an impression of our CI.

Target Market(s)

Small and medium-sized companies in Germany from the industry

Industry/Entity Type

Industrie, Handwerk

Contact Information for Business Card

Name, Position, Telefonnummer, Email, Website

Colors
EE7325
F08F49
F5BC92
FAE3D3
FDF4ED

Requirements
Must have
• A picture of the employee and in the style of www.valdringer-kollegen.de

```html
<!DOCTYPE html>
<html lang="de">
<head>
<meta charset="utf-8">
<title>Valdringer &amp; Kollegen – Visitenkarte</title>
<link rel="stylesheet" href="https://fonts.googleapis.com/css2?family=Montserrat:wght@400;500;600;700;800&display=swap">
<style>
  :root {
    --stage: #333333;
    --card-dark: #1a1a1a;
    --card-light: #ffffff;
    --accent: #f05a22;
    --text-dark: #1c1c1c;
    --text-light: #ffffff;
    --photo-top: #f4f4f4;
    --photo-bottom: #2a2a2e;
  }
  * { box-sizing: border-box; margin: 0; padding: 0; }
  html, body {
    width: 1200px; height: 1200px; overflow: hidden;
    background: var(--stage);
    font-family: "Montserrat", sans-serif;
  }
  .stage {
    width: 1200px; height: 1200px;
    display: flex; flex-direction: column; align-items: center; justify-content: center;
    gap: 60px;
  }
  .card {
    position: relative;
    width: 880px; height: 520px;
    border-radius: 34px;
    overflow: hidden;
    background: var(--card-dark);
    box-shadow: 0 14px 30px rgba(0,0,0,0.35);
  }
  .card-front .split { position: absolute; inset: 0; }
  .portrait {
    position: absolute; left: 128px; top: 100px;
    width: 250px; height: 216px;
  }
  .identity {
    position: absolute; left: 60px; width: 390px; top: 340px;
    text-align: center;
  }
  .identity .name {
    color: var(--accent); font-weight: 700; font-size: 34px; letter-spacing: 0.5px;
  }
  .identity .role {
    color: var(--text-light); font-weight: 500; font-size: 24px; margin-top: 2px;
  }
  .contact {
    position: absolute; left: 600px; top: 150px;
    list-style: none; color: var(--text-dark);
    font-size: 17px; font-weight: 500; line-height: 1.3;
  }
  .contact li { display: flex; align-items: flex-start; gap: 10px; margin-bottom: 10px; }
  .contact svg { flex: 0 0 20px; width: 20px; height: 20px; margin-top: 1px; }
  .card-back .brand {
    position: absolute; left: 0; right: 0; top: 190px;
    display: flex; align-items: center; justify-content: center; gap: 26px;
  }
  .brand-mark {
    width: 96px; height: 96px; background: var(--accent); flex: 0 0 96px;
  }
  .brand-name {
    color: var(--text-light); font-weight: 800; font-size: 50px;
    letter-spacing: 4px; line-height: 1.05; text-transform: uppercase;
  }
  .card-back .accent-bar {
    position: absolute; right: 0; bottom: 56px;
    width: 560px; height: 22px; background: var(--accent);
  }
</style>
</head>
<body>
<main class="stage">
  <section class="card card-front" aria-label="Visitenkarte Vorderseite">
    <svg class="split" width="880" height="520" viewBox="0 0 880 520" aria-hidden="true">
      <polygon points="452,0 880,0 880,520 648,520 578,262" fill="var(--card-light)"/>
      <polyline points="440,0 564,262 634,520" fill="none" stroke="var(--accent)" stroke-width="7"/>
    </svg>

    <svg class="portrait" viewBox="0 0 250 216" role="img" aria-label="Porträtfoto von Lukas Valdringer">
      <defs>
        <linearGradient id="photoTone" x1="0" y1="0" x2="0" y2="1">
          <stop offset="0" stop-color="var(--photo-top)"/>
          <stop offset="0.55" stop-color="#d9d7d6"/>
          <stop offset="1" stop-color="var(--photo-bottom)"/>
        </linearGradient>
      </defs>
      <polygon points="62,2 188,2 248,108 188,214 62,214 2,108" fill="url(#photoTone)" stroke="var(--accent)" stroke-width="3"/>
    </svg>

    <div class="identity">
      <p class="name">Lukas Valdringer</p>
      <p class="role">Gründer</p>
    </div>

    <ul class="contact">
      <li>
        <svg viewBox="0 0 24 24" aria-hidden="true"><path fill="var(--accent)" d="M6.6 10.8a15.1 15.1 0 0 0 6.6 6.6l2.2-2.2c.3-.3.7-.4 1-.2 1.1.4 2.3.6 3.6.6.6 0 1 .4 1 1V20c0 .6-.4 1-1 1A17 17 0 0 1 3 4c0-.6.4-1 1-1h3.5c.6 0 1 .4 1 1 0 1.3.2 2.5.6 3.6.1.3 0 .7-.2 1z"/></svg>
        <span>0171 492 3857</span>
      </li>
      <li>
        <svg viewBox="0 0 24 24" aria-hidden="true"><circle cx="12" cy="12" r="9.5" fill="none" stroke="var(--accent)" stroke-width="2"/><path d="M2.5 12h19M12 2.5c3 3 3 16 0 19M12 2.5c-3 3-3 16 0 19" fill="none" stroke="var(--accent)" stroke-width="1.6"/></svg>
        <span>www.valdringer-kollegen.de</span>
      </li>
      <li>
        <svg viewBox="0 0 24 24" aria-hidden="true"><rect x="2" y="5" width="20" height="14" fill="var(--accent)"/><path d="M2 5l10 8 10-8" fill="none" stroke="#fff" stroke-width="1.6"/></svg>
        <span>info@valdringer-kollegen.de</span>
      </li>
      <li>
        <svg viewBox="0 0 24 24" aria-hidden="true"><path fill="var(--accent)" d="M12 2a7 7 0 0 0-7 7c0 5.2 7 13 7 13s7-7.8 7-13a7 7 0 0 0-7-7zm0 9.6A2.6 2.6 0 1 1 12 6.4a2.6 2.6 0 0 1 0 5.2z"/></svg>
        <span>Valdringer &amp; Kollegen GmbH<br>Lindenhofer Straße 42b<br>72070 Rindenfeld</span>
      </li>
    </ul>
  </section>

  <section class="card card-back" aria-label="Visitenkarte Rückseite">
    <div class="brand">
      <span class="brand-mark" aria-hidden="true"></span>
      <p class="brand-name">Valdringer<br>&amp; Kollegen</p>
    </div>
    <span class="accent-bar" aria-hidden="true"></span>
  </section>
</main>
</body>
</html>
```